Business Card Design

We need a business card design for a new business based in Sutton, NH called 'Ridgecrest Repair'. We service home standby generators as well as other power equipment such as chainsaws, snowblowers and mowers. Our target audience is residential customers-hence the Ridgecrest slogan. "Ridgecrest Repair..." We would like to see designs that include a roof line and wrenches that would communicate this type of service. We would like to see designs that use the colors of orange, tan and dark green. The final design should communicate strong, reliable service....please incorporate a small Christian fish emblem somewhere in the design.

Target Market(s)

Residents who have standby generators and power equipment

Industry/Entity Type

Residential

Contact Information for Business Card

Ridgecrest Repair, Dale Fenwick, 817 Mapleford Ln, Alderbrook NH 03987, 603-555-0148 Cell: 603-555-0172

```html
<!DOCTYPE html>
<html lang="en">
<head>
<meta charset="utf-8">
<title>Ridgecrest Repair – Business Card</title>
<link rel="stylesheet" href="https://fonts.googleapis.com/css2?family=Marcellus+SC&family=Arimo:wght@400&display=swap">
<style>
  :root {
    --bg: #1c1c1c;
    --card: #ffffff;
    --orange: #f15a0f;
    --amber: #f7a21b;
    --yellow: #f5d314;
    --ink: #4a4a4a;
    --on-orange: #ffffff;
  }
  html, body {
    margin: 0;
    padding: 0;
    width: 1200px;
    height: 871px;
    overflow: hidden;
    background: var(--bg);
  }
  .canvas {
    position: relative;
    width: 1200px;
    height: 871px;
  }
  .card {
    position: absolute;
    left: 180px;
    top: 195px;
    width: 840px;
    height: 480px;
    background: var(--card);
    overflow: hidden;
    box-shadow: 0 20px 50px rgba(0,0,0,0.6);
  }
  .card__waves {
    position: absolute;
    inset: 0;
    width: 840px;
    height: 480px;
  }
  .brand {
    position: absolute;
    left: 70px;
    top: 40px;
    display: flex;
    align-items: center;
    gap: 24px;
  }
  .brand__dot {
    width: 50px;
    height: 50px;
    border-radius: 50%;
    background: var(--on-orange);
  }
  .brand__name {
    font-family: "Marcellus SC", serif;
    font-size: 42px;
    color: var(--on-orange);
    letter-spacing: 1px;
    margin: 0;
    font-weight: 400;
    white-space: nowrap;
  }
  .person {
    position: absolute;
    left: 60px;
    top: 225px;
    margin: 0;
    font-family: "Marcellus SC", serif;
    font-size: 34px;
    font-weight: 400;
    color: var(--orange);
    letter-spacing: 1px;
    white-space: nowrap;
  }
  .contact {
    position: absolute;
    left: 380px;
    top: 300px;
    margin: 0;
    padding: 0;
    list-style: none;
    font-family: "Arimo", sans-serif;
    font-size: 23px;
    color: var(--ink);
  }
  .contact__item {
    display: flex;
    align-items: center;
    gap: 14px;
    margin-bottom: 24px;
    white-space: nowrap;
  }
  .contact__icon {
    width: 22px;
    height: 26px;
    flex: none;
  }
</style>
</head>
<body>
<div class="canvas">
  <section class="card" aria-label="Ridgecrest Repair business card">
    <svg class="card__waves" viewBox="0 0 840 480" aria-hidden="true">
      <path d="M0 0 H840 V215 C720 200 600 150 450 150 C300 150 160 185 0 200 Z" fill="var(--yellow)"/>
      <path d="M0 0 H840 V198 C720 182 600 134 450 134 C300 134 160 168 0 183 Z" fill="var(--amber)"/>
      <path d="M0 0 H840 V182 C720 165 600 118 450 118 C300 118 160 150 0 165 Z" fill="var(--orange)"/>
    </svg>

    <div class="brand">
      <span class="brand__dot"></span>
      <h1 class="brand__name">Ridgecrest Repair</h1>
    </div>

    <h2 class="person">Dale Fenwick</h2>

    <ul class="contact">
      <li class="contact__item">
        <svg class="contact__icon" viewBox="0 0 22 26" aria-hidden="true">
          <path d="M11 1 C5.5 1 2 5 2 10 C2 16 11 25 11 25 C11 25 20 16 20 10 C20 5 16.5 1 11 1 Z" fill="var(--amber)"/>
          <circle cx="11" cy="10" r="3.5" fill="#fff"/>
        </svg>
        <span>817 Mapleford Ln, Alderbrook NH 03987</span>
      </li>
      <li class="contact__item">
        <svg class="contact__icon" viewBox="0 0 22 26" aria-hidden="true">
          <path d="M5 2 L9 2 L10.5 8 L7.5 10 C8.5 13.5 10.5 16.5 13.5 18.5 L16 15.5 L21 17.5 L20.5 22 C19.5 24 16 24.5 12 22 C6 18 2.5 11 3 6 C3.2 3.8 3.8 2.5 5 2 Z" fill="var(--amber)"/>
        </svg>
        <span>603-555-0148, 603-555-0172</span>
      </li>
    </ul>
  </section>
</div>
</body>
</html>
```